I need an out door banner to help me promote my classes, i am a dating coach. i would like to see designs that use the colors. black, yellow, pink, white,orange. colors that attract women. the final design should communicate how women can Reclaim Every Spark, Shine Once More.

Target Market(s)

Bright Mornings After Midnight Storms: Reclaim Every Spark, Shine Once More: Heartfelt Wisdom on Modern Courtship

Industry/Entity Type

dating advice

Logo Text

Attention Ladies: Weed out the Narcissist, the abusers, the couch potatoes, the players & the losers...( Expose & Dump his #ss before he destroys your life)

Colors

Designer to choose colors to be used in the design.

Requirements
Nice to have
• Some bold text too
Should not have
• black round

```html
<!DOCTYPE html>
<html lang="en">
<head>
<meta charset="utf-8">
<title>Attention Ladies – Outdoor Banner</title>
<link rel="stylesheet" href="https://fonts.googleapis.com/css2?family=Montserrat:wght@400;500;600;700&display=swap">
<style>
  :root {
    --page-bg: #fff7fb;
    --brand-pink: #ec3e94;
    --ink: #111111;
    --paper: #ffffff;
  }
  html, body {
    margin: 0;
    padding: 0;
    width: 809px;
    height: 1200px;
    overflow: hidden;
    background: var(--page-bg);
  }
  .canvas {
    position: relative;
    width: 809px;
    height: 1200px;
    display: flex;
    align-items: center;
    justify-content: center;
  }
  .banner {
    width: 663px;
    height: 1100px;
    display: block;
  }
  .banner text {
    font-family: "Montserrat", sans-serif;
  }
  .banner__field { fill: var(--brand-pink); }
  .banner__strip { fill: var(--paper); }
  .word--ink { fill: var(--ink); }
  .word--light { fill: var(--paper); }
  .word--pink { fill: var(--brand-pink); }
  .word--bold { font-weight: 700; }
  .word--semi { font-weight: 600; }
  .word--regular { font-weight: 400; }
</style>
</head>
<body>
<main class="canvas">
  <svg class="banner" viewBox="0 0 522 866" xmlns="http://www.w3.org/2000/svg" role="img"
       aria-label="Attention ladies, weed out the narcissist, the abusers, the couch potatoes, the players and the losers. Expose and dump his #ss before he destroys your life.">
    <rect class="banner__field" x="0" y="0" width="522" height="774"/>
    <rect class="banner__strip" x="0" y="774" width="522" height="92"/>

    <g class="headline">
      <text class="word--ink word--bold" x="62" y="128" font-size="88" textLength="393" lengthAdjust="spacingAndGlyphs">Attention</text>
      <text class="word--light word--semi" x="62" y="198" font-size="74" textLength="393" lengthAdjust="spacing">LADIES</text>
      <text class="word--light word--semi" x="62" y="276" font-size="82" textLength="310" lengthAdjust="spacing">WEED</text>
      <text class="word--ink word--semi" x="393" y="244" font-size="38" textLength="62" lengthAdjust="spacingAndGlyphs">out</text>
      <text class="word--ink word--semi" x="393" y="277" font-size="38" textLength="62" lengthAdjust="spacingAndGlyphs">the</text>
      <text class="word--ink word--bold" x="62" y="354" font-size="90" textLength="393" lengthAdjust="spacingAndGlyphs">Narcissist</text>
      <text class="word--light word--semi" transform="translate(91 493) rotate(-90)" font-size="42" textLength="122" lengthAdjust="spacing">THE</text>
      <text class="word--ink word--bold" x="118" y="415" font-size="61" textLength="337" lengthAdjust="spacingAndGlyphs">ABUSERS</text>
      <text class="word--light word--semi" x="118" y="498" font-size="88" textLength="337" lengthAdjust="spacingAndGlyphs">COUCH</text>
      <text class="word--light word--semi" x="62" y="567" font-size="71" textLength="393" lengthAdjust="spacingAndGlyphs">POTATOES</text>
      <text class="word--ink word--bold" transform="translate(86 637) rotate(-90)" font-size="30" textLength="49" lengthAdjust="spacingAndGlyphs">the</text>
      <text class="word--ink word--bold" x="100" y="635" font-size="71" textLength="355" lengthAdjust="spacingAndGlyphs">PLAYERS</text>
      <text class="word--ink word--semi" x="62" y="678" font-size="34" textLength="60" lengthAdjust="spacingAndGlyphs">and</text>
      <text class="word--ink word--semi" x="62" y="711" font-size="34" textLength="60" lengthAdjust="spacing">the</text>
      <text class="word--light word--semi" x="137" y="711" font-size="82" textLength="318" lengthAdjust="spacingAndGlyphs">LOSERS</text>
    </g>

    <g class="tagline">
      <text class="word--ink word--regular" x="169" y="801" font-size="16" textLength="191" lengthAdjust="spacing">EXPOSE &amp; DUMP</text>
      <text class="word--ink word--regular" transform="translate(102 852) rotate(-90)" font-size="16" textLength="37" lengthAdjust="spacing">HIS</text>
      <text class="word--pink word--bold" x="130" y="849" font-size="40" textLength="92" lengthAdjust="spacingAndGlyphs">#SS</text>
      <text class="word--ink word--regular" x="245" y="826" font-size="13" textLength="191" lengthAdjust="spacing">BEFORE HE DESTROYS</text>
      <text class="word--pink word--semi" x="245" y="851" font-size="20" textLength="192" lengthAdjust="spacing">YOUR LIFE</text>
    </g>
  </svg>
</main>
</body>
</html>
```